Business Card Design Project

I need a business card for an environmentally friendly interior design company called Maplecrest Decor.
I was thinking it might be nice to print the business cards on brown recycled paper with green ink.
In addition to interior design, I will also be able to consult with homeowners regarding their indoor environments and how they might be affecting their health after May 2013 which is when I will complete my certification program. This can be added to the business card at that time: "Certified Dwelling Vitality Environmental Consultant".

```html
<!DOCTYPE html>
<html lang="en">
<head>
<meta charset="utf-8">
<title>Maplecrest Decor – Business Card</title>
<link rel="stylesheet" href="https://fonts.googleapis.com/css2?family=Federo&family=Source+Sans+3:wght@400;600&display=swap">
<style>
  :root {
    --paper-brown: #97530e;
    --gap-white: #ffffff;
    --ink-lime: #9cc31e;
    --ink-green: #72ad2c;
    --ink-title: #6fae3a;
  }
  * { margin: 0; padding: 0; box-sizing: border-box; }
  html, body {
    width: 1200px;
    height: 329px;
    overflow: hidden;
    background: var(--gap-white);
  }
  .sheet {
    position: relative;
    width: 1200px;
    height: 329px;
  }
  .card {
    position: absolute;
    top: 0;
    width: 558px;
    height: 329px;
    background: var(--paper-brown);
  }
  .card--front { left: 0; }
  .card--back { left: 642px; }

  .brand-mark {
    position: absolute;
    left: 0;
    top: 0;
    width: 558px;
    height: 329px;
    display: flex;
    align-items: center;
    justify-content: center;
    gap: 18px;
  }
  .brand-mark__dot {
    width: 64px;
    height: 64px;
    border-radius: 50%;
    background: var(--ink-lime);
  }
  .brand-mark__name {
    font-family: "Source Sans 3", sans-serif;
    font-weight: 600;
    font-size: 36px;
    color: var(--ink-lime);
  }

  .details {
    position: absolute;
    left: 26px;
    top: 14px;
    right: 20px;
    font-family: "Source Sans 3", sans-serif;
    color: var(--ink-lime);
  }
  .details__company {
    font-family: "Federo", sans-serif;
    font-weight: 400;
    font-size: 36px;
    line-height: 44px;
    color: var(--ink-title);
  }
  .details__tagline {
    margin-top: 30px;
    font-size: 21px;
    line-height: 26px;
  }
  .details__credential {
    margin-top: 15px;
    font-size: 21px;
    line-height: 28px;
    max-width: 450px;
  }
  .contact {
    position: absolute;
    left: 26px;
    top: 240px;
    font-family: "Source Sans 3", sans-serif;
    font-weight: 600;
    font-size: 20px;
    line-height: 28px;
    color: var(--ink-green);
  }
</style>
</head>
<body>
  <main class="sheet">
    <section class="card card--front">
      <div class="brand-mark">
        <span class="brand-mark__dot"></span>
        <span class="brand-mark__name">Maplecrest Decor</span>
      </div>
    </section>

    <section class="card card--back">
      <div class="details">
        <h1 class="details__company">Maplecrest Decor</h1>
        <p class="details__tagline">Environmentally friendly design</p>
        <p class="details__credential">Certified Dwelling Vitality Environmental Consultant</p>
      </div>
      <address class="contact">
        <div class="contact__name">Clara Dawn Ellis</div>
        <div class="contact__phone">713-555-0148</div>
      </address>
    </section>
  </main>
</body>
</html>
```